Flyer-Design für Software für Gebäudedienstleister
Zielgruppe
Software für Gebäudedienstleister,
Softwarevertrieb, Durchführung von Schulungen,
Aufgabenstellung
Erstellt werden soll eine Din A4 Seite mit Wickelfalz (6Seiten)
Für den Neustart einer Software für Gebäudedienstleister möchten wir einen modernen
Flyer mit ansprechendem Text anfertigen lassen.
Die Software funktioniert Online oder Lokal.
Ein Tablet-Service wird angeboten.
Eine elektronische Planungstafel bietet die Software.
Terminplanung mittels "Drag & Drop" möglich
1-Klick Funktion in der Rückmeldung von Arbeitsscheinen und in der anschließenden Fakturierung.
Durchführung von Schulungen Akademie
Texte:
1.Fakturierung
Mit Vantoruk® Faktura liefern wir Ihnen ein leicht zu bedienendes Modul
Die Vantoruk®Fakturierungssoftware zeichnet sich durch einfache Handhabung aus:
Moderne Faktura Software
Leicht zu bedienen
Gut strukturierte Benutzeroberfläche
Praxisorientierte Funktionen
Sofort einsatzbereit
1-Klick Fakturierung
Mit Vantoruk® fakturieren Sie schnell und effektiv.
2. Personaleinsatzplanung Drag & Drop
Die Einsatzplanung erfolgt in Vantoruk® mit nur wenigen Schritten.
Dabei berücksichtigt das System z.B. die Regionen, in denen Sie
tätig sind und verhindert somit unnötige Fahrzeiten.
Pausen werden automatisch erfasst. Touren planen Sie bereits
bequem per Drag & Drop auf dem Gesamtkalender.
3. Planungstafel
Mit Vantoruk® planen Sie einfach und schnell Termine.
Mit unserer elektronischen Planungstafel behalten Sie immer
einen optimalen Überblick über Ihre Ressourcen.
Vantoruk® ist die intelligente Lösung für Ihre Personaleinsatzplanung.
4. Tabletservice
Bieten Sie Ihrem Kunden mit Vantoruk® einen echten Mehrwert
Sie möchten Ihrem Kunden gegenüber als modernes und zielorientiertes
Unternehmen auftreten?
Setzen Sie ab jetzt unseren Tablet-Service in Ihrem Betrieb ein.
Egal ob Arbeitsschein zurückmelden, schnell ein Foto vom Wintergarten,
oder eine Unterschrift fü..

```html
<!DOCTYPE html>
<html lang="de">
<head>
<meta charset="utf-8">
<title>Vantoruk – Wickelfalz-Flyer Präsentation</title>
<link href="https://fonts.googleapis.com/css2?family=Quicksand:wght@400;500;600&family=Questrial&display=swap" rel="stylesheet">
<style>
  :root {
    --green: #adb935;
    --slate: #5c6075;
    --ink: #5a5e6e;
    --paper: #ffffff;
    --board: #ffffff;
    --label: #1a1a1a;
  }
  html, body {
    margin: 0;
    padding: 0;
    width: 1200px;
    height: 1200px;
    overflow: hidden;
    background: var(--board);
  }
  .board {
    position: relative;
    width: 1200px;
    height: 1200px;
  }
  .panel {
    position: absolute;
    background: var(--paper);
    box-shadow: 2px 4px 6px rgba(0,0,0,0.35);
    display: block;
  }
  .panel--outside { left: 187px; top: 87px; width: 592px; height: 419px; }
  .panel--cover   { left: 823px; top: 87px; width: 196px; height: 419px; }
  .panel--inside  { left: 187px; top: 587px; width: 592px; height: 419px; }
  .panel--back    { left: 824px; top: 587px; width: 197px; height: 419px; }

  .board-label {
    position: absolute;
    margin: 0;
    font-family: "Questrial", sans-serif;
    font-size: 25px;
    font-weight: 400;
    letter-spacing: 1.5px;
    color: var(--label);
  }
  .board-label--outside { left: 214px; top: 518px; }
  .board-label--cover   { left: 886px; top: 523px; }
  .board-label--inside  { left: 214px; top: 1028px; }
  .board-label--back    { left: 873px; top: 1025px; }

  svg text { font-family: "Quicksand", sans-serif; }
  .t-heading { font-size: 33px; font-weight: 400; fill: var(--ink); }
  .t-heading--green { fill: var(--green); }
  .t-body { font-size: 10.5px; fill: var(--ink); }
  .t-list { font-size: 14px; fill: #ffffff; }
  .t-small-list { font-size: 10.5px; fill: var(--ink); }
  .t-address { font-size: 11px; fill: #ffffff; }
  .t-title-big { font-size: 52px; fill: #ffffff; }
  .t-title { font-size: 35px; fill: #ffffff; }
  .t-title-long { font-size: 32px; fill: #ffffff; }
  .t-title-small { font-size: 29px; fill: #ffffff; }
  .t-brand { font-size: 36px; font-weight: 600; fill: #ffffff; }
  .t-brand-tag { font-size: 8px; font-weight: 600; fill: #ffffff; letter-spacing: 1px; }
  .t-table { font-size: 4px; fill: #555; }
  .t-table-head { font-size: 5px; font-weight: 600; fill: #444; }
  .shape-green { fill: var(--green); }
  .shape-slate { fill: var(--slate); }
  .frame-line { stroke: var(--slate); stroke-width: 1.2; fill: none; }
  .frame-line--thin { stroke: var(--slate); stroke-width: 1; fill: none; }
</style>
</head>
<body>
<main class="board">

  <svg width="0" height="0" style="position:absolute" aria-hidden="true">
    <defs>
      <linearGradient id="grad-building" x1="0" y1="0" x2="1" y2="1">
        <stop offset="0" stop-color="#8a93a3"/>
        <stop offset="0.5" stop-color="#c9d2de"/>
        <stop offset="1" stop-color="#e6e9ee"/>
      </linearGradient>
      <linearGradient id="grad-desk" x1="0" y1="0" x2="0" y2="1">
        <stop offset="0" stop-color="#f2f3f5"/>
        <stop offset="1" stop-color="#d9dce1"/>
      </linearGradient>
      <linearGradient id="grad-notes" x1="0" y1="0" x2="1" y2="1">
        <stop offset="0" stop-color="#b6cc3a"/>
        <stop offset="0.5" stop-color="#9aa07a"/>
        <stop offset="1" stop-color="#b6cc3a"/>
      </linearGradient>
      <linearGradient id="grad-campus" x1="0" y1="0" x2="0" y2="1">
        <stop offset="0" stop-color="#9ea9bd"/>
        <stop offset="0.55" stop-color="#6b5a52"/>
        <stop offset="1" stop-color="#6f7d55"/>
      </linearGradient>
      <linearGradient id="grad-tablet" x1="0" y1="0" x2="1" y2="1">
        <stop offset="0" stop-color="#8db33a"/>
        <stop offset="1" stop-color="#b7d157"/>
      </linearGradient>

      <symbol id="schedule-table" viewBox="0 0 290 95">
        <text class="t-table-head" x="0" y="5">Terminplaner</text>
        <g fill="#adb935">
          <rect x="12" y="11" width="34" height="6"/>
          <rect x="49" y="11" width="30" height="6"/>
          <rect x="82" y="11" width="16" height="6"/>
          <rect x="101" y="11" width="10" height="6"/>
          <rect x="114" y="11" width="12" height="6"/>
          <rect x="129" y="11" width="12" height="6"/>
          <rect x="144" y="11" width="12" height="6"/>
          <rect x="212" y="11" width="12" height="6"/>
          <rect x="227" y="11" width="14" height="6"/>
          <rect x="244" y="11" width="14" height="6"/>
          <rect x="261" y="11" width="14" height="6"/>
        </g>
        <text class="t-table" x="166" y="16">Freitag 14.04.</text>
        <g stroke="#c9c9c9" stroke-width="0.5" fill="none">
          <rect x="0" y="22" width="290" height="73"/>
          <line x1="0" y1="33" x2="290" y2="33"/>
          <line x1="58" y1="22" x2="58" y2="95"/>
          <line x1="58" y1="27" x2="290" y2="27"/>
          <line x1="0" y1="42" x2="290" y2="42"/>
          <line x1="0" y1="51" x2="290" y2="51"/>
          <line x1="0" y1="60" x2="290" y2="60"/>
          <line x1="0" y1="69" x2="290" y2="69"/>
          <line x1="0" y1="78" x2="290" y2="78"/>
          <line x1="0" y1="87" x2="290" y2="87"/>
        </g>
        <g stroke="#e2e2e2" stroke-width="0.4">
          <line x1="70" y1="27" x2="70" y2="95"/><line x1="82" y1="27" x2="82" y2="95"/>
          <line x1="94" y1="27" x2="94" y2="95"/><line x1="106" y1="27" x2="106" y2="95"/>
          <line x1="118" y1="27" x2="118" y2="95"/><line x1="130" y1="27" x2="130" y2="95"/>
          <line x1="142" y1="27" x2="142" y2="95"/><line x1="154" y1="27" x2="154" y2="95"/>
          <line x1="166" y1="27" x2="166" y2="95"/><line x1="178" y1="27" x2="178" y2="95"/>
          <line x1="190" y1="27" x2="190" y2="95"/><line x1="202" y1="27" x2="202" y2="95"/>
          <line x1="214" y1="27" x2="214" y2="95"/><line x1="226" y1="27" x2="226" y2="95"/>
          <line x1="238" y1="27" x2="238" y2="95"/><line x1="250" y1="27" x2="250" y2="95"/>
          <line x1="262" y1="27" x2="262" y2="95"/><line x1="274" y1="27" x2="274" y2="95"/>
        </g>
        <rect x="106" y="33" width="6" height="62" fill="#f3d3d6"/>
        <rect x="180" y="33" width="6" height="62" fill="#f3d3d6"/>
        <text class="t-table" x="180" y="26">Freitag 14.04.</text>
        <text class="t-table" x="3" y="48">Team Nord</text>
        <text class="t-table" x="3" y="57">Team Süd</text>
        <text class="t-table" x="3" y="66">Team West</text>
        <text class="t-table" x="3" y="75">Team Ost</text>
        <text class="t-table" x="3" y="84">Team Mitte</text>
        <text class="t-table" x="3" y="93">Reserve</text>
        <rect x="260" y="43" width="28" height="7" fill="#bcd0e4"/>
        <rect x="84" y="52" width="24" height="7" fill="#cfc7a0"/>
        <rect x="236" y="52" width="50" height="7" fill="#cfc7a0"/>
        <rect x="112" y="61" width="30" height="7" fill="#dfe9c8"/>
        <rect x="190" y="61" width="24" height="7" fill="#cfe0ea"/>
        <rect x="84" y="70" width="134" height="7" fill="#9ec4e4"/>
        <rect x="250" y="79" width="26" height="7" fill="#cfe0ea"/>
      </symbol>

      <symbol id="outside-spread" viewBox="0 0 948 670">
        <rect x="0" y="0" width="948" height="670" fill="#ffffff"/>
        <polyline class="frame-line" points="14,0 14,63 285,63"/>
        <polygon class="shape-slate" points="245,0 316,0 316,95"/>
        <text class="t-heading" x="38" y="51">Fakturierung</text>
        <text class="t-body">
          <tspan x="25" y="112">Lorem ipsum dolor sit amet, consectetuer adipiscing</tspan>
          <tspan x="25" y="123.5">elit. Aenean commodo ligula eget dolor. Aenean</tspan>
          <tspan x="25" y="135">massa. Cum sociis natoque penatibus et magnis dis</tspan>
          <tspan x="25" y="146.5">parturient montes, nascetur ridiculus mus. Donec quam</tspan>
          <tspan x="25" y="158">felis, ultricies nec, pellentesque eu, pretium quis, sem.</tspan>
          <tspan x="25" y="169.5">Nulla consequat massa quis enim. Donec pede justo,</tspan>
          <tspan x="25" y="181">fringilla vel, aliquet nec, vulputate eget, arcu.</tspan>
        </text>
        <g fill="var(--green)">
          <circle cx="28" cy="206" r="1.5"/><circle cx="28" cy="217.5" r="1.5"/>
          <circle cx="28" cy="229" r="1.5"/><circle cx="28" cy="240.5" r="1.5"/>
          <circle cx="28" cy="252" r="1.5"/><circle cx="28" cy="263.5" r="1.5"/>
        </g>
        <text class="t-body">
          <tspan x="34" y="209.5">Lorem ipsum</tspan>
          <tspan x="34" y="221">Lorem ipsum</tspan>
          <tspan x="34" y="232.5">Lorem ipsum</tspan>
          <tspan x="34" y="244">Lorem ipsum</tspan>
          <tspan x="34" y="255.5">Lorem ipsum</tspan>
          <tspan x="34" y="267">Lorem ipsum</tspan>
        </text>
        <text class="t-body">
          <tspan x="25" y="309">Lorem ipsum dolor sit amet, consectetuer adipiscing</tspan>
          <tspan x="25" y="320.5">elit. Aenean commodo ligula eget dolor. Aenean</tspan>
          <tspan x="25" y="332">massa. Cum sociis natoque penatibus et magnis dis</tspan>
          <tspan x="25" y="343.5">parturient montes, nascetur ridiculus mus. Donec quam</tspan>
          <tspan x="25" y="355">felis, ultricies nec, pellentesque eu, pretium quis, sem.</tspan>
        </text>
        <rect x="0" y="420" width="316" height="250" fill="url(#grad-desk)" role="img" aria-label="Foto: Schreibtisch mit Laptop, Monitor mit Balkendiagramm und Kaffeetasse"/>

        <polygon class="shape-slate" points="316,349 353,312 619,577 529,670 316,670"/>
        <text class="t-address">
          <tspan x="352" y="544">Adresse</tspan>
          <tspan x="352" y="557">Strasse</tspan>
          <tspan x="352" y="570">PLZ, Ort</tspan>
          <tspan x="352" y="583">Tel</tspan>
          <tspan x="352" y="596">Mail</tspan>
          <tspan x="352" y="609">www</tspan>
        </text>

        <polygon points="646,0 948,0 948,283 925,283" fill="url(#grad-building)" role="img" aria-label="Foto: moderne geschwungene Bürogebäude unter blauem Himmel"/>
        <polygon class="shape-slate" points="915,312 948,345 948,670 737,670 646,577"/>
        <polygon class="shape-green" points="631,30 899,297 631,564 364,297"/>
        <polygon class="frame-line--thin" points="613,30 899,282 646,563 364,311"/>
        <text class="t-title-big" x="641" y="215" textLength="77" lengthAdjust="spacingAndGlyphs">DIE</text>
        <text class="t-title" x="644" y="263" textLength="155" lengthAdjust="spacingAndGlyphs">Software</text>
        <text class="t-title-small" x="644" y="302" textLength="33" lengthAdjust="spacingAndGlyphs">für</text>
        <text class="t-title-long" x="645" y="339" textLength="147" lengthAdjust="spacingAndGlyphs">Gebäude-</text>
        <text class="t-title-long" x="645" y="373" textLength="160" lengthAdjust="spacingAndGlyphs">dienstleister</text>
        <text class="t-brand" x="712" y="597">Vantoruk</text>
        <text class="t-brand-tag" x="731" y="609">SOFTWARE FÜR GEBÄUDEDIENSTLEISTER</text>
      </symbol>
    </defs>
  </svg>

  <svg class="panel panel--outside" viewBox="0 0 948 670" role="group" aria-label="Flyer Aussenseite">
    <use href="#outside-spread" x="0" y="0" width="948" height="670"/>
  </svg>
  <p class="board-label board-label--outside">aussen</p>

  <svg class="panel panel--cover" viewBox="632 0 316 670" role="group" aria-label="Flyer Titelseite">
    <use href="#outside-spread" x="0" y="0" width="948" height="670"/>
  </svg>
  <p class="board-label board-label--cover">Titel</p>

  <svg class="panel panel--inside" viewBox="0 0 948 670" role="group" aria-label="Flyer Innenseite">
    <rect x="0" y="0" width="948" height="670" fill="#ffffff"/>

    <polygon class="shape-green" points="0,0 22,0 49,28 12,65 0,65"/>
    <polyline class="frame-line" points="12,63 304,63 304,0"/>
    <text class="t-heading t-heading--green" x="81" y="43">Planungstafel</text>
    <text class="t-body">
      <tspan x="22" y="106">Lorem ipsum dolor sit amet, consectetuer adipiscing elit.</tspan>
      <tspan x="22" y="117.5">Aenean commodo ligula eget dolor. Aenean massa. Cum</tspan>
      <tspan x="22" y="129">sociis natoque penatibus et magnis dis parturient montes,</tspan>
      <tspan x="22" y="140.5">nascetur ridiculus mus. Donec quam felis, ultricies nec,</tspan>
      <tspan x="22" y="152">pellentesque eu, pretium quis, sem. Nulla consequat mas-</tspan>
      <tspan x="22" y="163.5">sa quis enim. Donec pede justo, fringilla vel, aliquet nec,</tspan>
      <tspan x="22" y="175">vulputate eget, arcu.</tspan>
    </text>
    <use href="#schedule-table" x="14" y="210" width="290" height="95"/>

    <polygon class="shape-slate" points="241,378 316,303 316,453"/>
    <polyline class="frame-line" points="241,378 13,378 13,442 316,442"/>
    <text class="t-heading" x="20" y="422">Drag &amp; Drop</text>
    <text class="t-body">
      <tspan x="25" y="487">Lorem ipsum dolor sit amet, consectetuer adipiscing</tspan>
      <tspan x="25" y="498.5">elit. Aenean commodo ligula eget dolor. Aenean</tspan>
      <tspan x="25" y="510">massa. Cum sociis natoque penatibus et magnis dis</tspan>
      <tspan x="25" y="521.5">parturient montes, nascetur ridiculus mus. Donec quam</tspan>
      <tspan x="25" y="533">felis, ultricies nec, pellentesque eu, pretium quis, sem.</tspan>
      <tspan x="25" y="544.5">Nulla consequat massa quis enim. Donec pede justo,</tspan>
      <tspan x="25" y="556">fringilla vel, aliquet nec, vulputate eget, arcu.</tspan>
    </text>
    <use href="#schedule-table" x="14" y="580" width="290" height="95"/>

    <rect x="329" y="0" width="303" height="165" fill="url(#grad-notes)" role="img" aria-label="Foto: Mann hinter einer Glaswand voller grüner Haftnotizen"/>

    <polygon class="shape-slate" points="888,0 948,0 948,105 864,23"/>
    <polyline class="frame-line" points="645,0 645,63 903,63"/>
    <text class="t-heading" x="658" y="43">Akademie</text>
    <text class="t-body">
      <tspan x="645" y="106">Lorem ipsum dolor sit amet, consectetuer adipiscing elit.</tspan>
      <tspan x="645" y="117.5">Aenean commodo ligula eget dolor. Aenean massa. Cum</tspan>
      <tspan x="645" y="129">sociis natoque penatibus et magnis dis parturient montes,</tspan>
      <tspan x="645" y="140.5">nascetur ridiculus mus. Donec quam felis, ultricies nec,</tspan>
    </text>
    <g class="shape-slate">
      <rect x="682" y="172" width="6" height="6" transform="rotate(45 685 175)"/>
      <rect x="682" y="190" width="6" height="6" transform="rotate(45 685 193)"/>
      <rect x="682" y="208" width="6" height="6" transform="rotate(45 685 211)"/>
      <rect x="682" y="226" width="6" height="6" transform="rotate(45 685 229)"/>
    </g>
    <text class="t-small-list">
      <tspan x="693" y="179">Schulung 1</tspan>
      <tspan x="693" y="197">Schulung 2</tspan>
      <tspan x="693" y="215">Schulung 3</tspan>
      <tspan x="693" y="233">Schulung 4</tspan>
    </text>
    <rect x="645" y="270" width="291" height="113" fill="url(#grad-campus)" role="img" aria-label="Foto: geschwungenes Schulungsgebäude mit Rasenfläche"/>

    <polyline class="frame-line" points="690,436 936,436 936,513 640,513"/>

    <polygon class="shape-green" points="439,182 706,448 488,670 391,670 316,595 316,305"/>
    <g fill="var(--slate)">
      <rect x="374" y="336" width="7" height="7" transform="rotate(45 377.5 339.5)"/>
      <rect x="374" y="368" width="7" height="7" transform="rotate(45 377.5 371.5)"/>
      <rect x="374" y="401" width="7" height="7" transform="rotate(45 377.5 404.5)"/>
      <rect x="374" y="433" width="7" height="7" transform="rotate(45 377.5 436.5)"/>
      <rect x="374" y="466" width="7" height="7" transform="rotate(45 377.5 469.5)"/>
      <rect x="374" y="498" width="7" height="7" transform="rotate(45 377.5 501.5)"/>
      <rect x="374" y="531" width="7" height="7" transform="rotate(45 377.5 534.5)"/>
      <rect x="374" y="563" width="7" height="7" transform="rotate(45 377.5 566.5)"/>
    </g>
    <text class="t-list">
      <tspan x="398" y="345">Online oder Lokal</tspan>
      <tspan x="398" y="377">Personaleinsatzplanung</tspan>
      <tspan x="398" y="410">Kunden, Objekte, Auftrag</tspan>
      <tspan x="398" y="442">Fakturierung</tspan>
      <tspan x="398" y="475">Artikelverkauf</tspan>
      <tspan x="398" y="507">Wartungsplaner</tspan>
      <tspan x="398" y="540">Datenschnittstellen</tspan>
      <tspan x="398" y="572">Akademie, Schulungen</tspan>
    </text>

    <text class="t-heading t-heading--green" x="704" y="485">Tabletservice</text>
    <text class="t-body">
      <tspan x="645" y="566">Lorem ipsum dolor sit amet,</tspan>
      <tspan x="645" y="577.5">consectetuer adipiscing elit.</tspan>
      <tspan x="645" y="589">Aenean commodo ligula eget</tspan>
      <tspan x="645" y="600.5">dolor. Aenean massa. Cum</tspan>
      <tspan x="645" y="612">sociis natoque penatibus et</tspan>
      <tspan x="645" y="623.5">magnis dis parturient montes,</tspan>
      <tspan x="645" y="635">nascetur ridiculus mus.</tspan>
    </text>
    <rect x="813" y="558" width="123" height="80" fill="url(#grad-tablet)" role="img" aria-label="Illustration: Tablet mit Arbeitsschein"/>
  </svg>
  <p class="board-label board-label--inside">innen</p>

  <svg class="panel panel--back" viewBox="0 0 315 670" role="group" aria-label="Flyer Rückseite">
    <rect x="0" y="0" width="315" height="670" fill="#ffffff"/>
    <polygon class="shape-green" points="315,22 315,560 47,300"/>
    <polygon class="shape-slate" points="0,343 32,311 302,578 212,670 0,670"/>
    <polyline class="frame-line--thin" points="315,48 295,28 47,312 315,575"/>
    <text class="t-address">
      <tspan x="34" y="542">Adresse</tspan>
      <tspan x="34" y="555">Strasse</tspan>
      <tspan x="34" y="568">PLZ, Ort</tspan>
      <tspan x="34" y="581">Tel</tspan>
      <tspan x="34" y="594">Mail</tspan>
      <tspan x="34" y="607">www</tspan>
    </text>
  </svg>
  <p class="board-label board-label--back">Rückseite</p>

</main>
</body>
</html>
```